KT ELECTRICAL SERVICES

I am just setting up on my own as an electrician. I want a 2 sided business card that is eye catching on the front and has skills on the back. I do domestic, commercial and agricultural work.
Inspection and Testing.
Rewires.
Fuseboards.
New builds.
Fault finding.
Free quotations
All work undertaken.
10 years experience.
Registered and insured by VORSEC.
Customer references available on request.
Kevin Tallis. Mob. 07700900461. Home 01632960418.
Email. merrow.kt@postvale.com.
My own unique logo would be nice either electrical related or KT initial related.
After seeing all the designs I prefer something simple but striking. My favourite so far is just black background blue and red writing and is simple but striking. And a KT with something electrical incorporated into it.

Industry/Entity Type

Electrical

Requirements
Must have
• Services and a good logo or graphic.

```html
<!DOCTYPE html>
<html lang="en">
<head>
<meta charset="utf-8">
<title>KT Electrical Services – Business Card</title>
<link rel="stylesheet" href="https://fonts.googleapis.com/css2?family=Courier+Prime:wght@400;700&family=Exo+2:ital,wght@0,600;1,900&family=Oswald:wght@700&family=Tinos:wght@400;700&display=swap">
<style>
  :root {
    --page: #2a2d33;
    --card-deep: #0b0a2e;
    --card-mid: #1c1f6e;
    --card-glow: #2e3db0;
    --band-blue: #3a3fb4;
    --band-light: #4b52d0;
    --glow-pale: #9fdcff;
    --glow-blue: #2f7fe0;
    --logo-yellow: #f2ec1f;
    --text-white: #ffffff;
    --hex-border: #ffffff;
  }
  * { box-sizing: border-box; margin: 0; padding: 0; }
  html, body { width: 1200px; height: 1200px; overflow: hidden; background: var(--page); }
  .canvas { position: relative; width: 1200px; height: 1200px; }

  .card {
    position: absolute; left: 100px; width: 1000px; height: 560px;
    overflow: hidden; border-radius: 4px;
    background: radial-gradient(ellipse at 50% 50%, var(--card-glow) 0%, var(--card-mid) 40%, var(--card-deep) 85%);
    box-shadow: 0 10px 30px rgba(0,0,0,.45);
  }
  .card--back { top: 25px; }
  .card--front { top: 615px; }

  /* Artwork areas: soft glow placeholders */
  .glow-band {
    position: absolute; left: 0; width: 100%;
    background: radial-gradient(ellipse 60% 70% at 50% 50%, rgba(159,220,255,.55) 0%, rgba(47,127,224,.35) 40%, rgba(47,127,224,0) 100%);
  }
  .card--back .glow-band--top { top: 0; height: 80px; }
  .card--back .glow-band--bottom { bottom: 0; height: 130px; }
  .card--front .glow-band--top { top: 0; height: 95px; }

  /* Services list */
  .services {
    position: absolute; left: 60px; top: 92px; list-style: none;
    font-family: "Courier Prime", "Courier New", monospace; font-weight: 700;
    font-size: 27px; line-height: 38px; color: var(--text-white);
  }
  .services li { display: flex; align-items: center; gap: 10px; white-space: nowrap; }
  .services svg { width: 18px; height: 24px; flex: none; }

  /* Name mark */
  .brand {
    position: absolute; display: flex; align-items: center; gap: 16px;
    font-family: "Oswald", "Arial Narrow", sans-serif; font-weight: 700;
    color: var(--logo-yellow); line-height: 1;
  }
  .brand__square { width: 22px; height: 22px; background: var(--logo-yellow); flex: none; }
  .brand__name { font-size: 44px; letter-spacing: 1px; }
  .card--back .brand { right: 60px; top: 205px; }
  .card--front .brand { right: 60px; top: 130px; }

  /* Front side */
  .holder-name {
    position: absolute; left: 55px; top: 110px;
    font-family: "Exo 2", sans-serif; font-weight: 600; font-size: 54px;
    color: var(--text-white);
  }
  .contact-band {
    position: absolute; left: 0; top: 240px; width: 660px; height: 155px;
    background: linear-gradient(90deg, var(--band-light), var(--band-blue));
    clip-path: polygon(0 0, 100% 0, 94% 100%, 0 100%);
    padding: 18px 0 0 50px;
    font-family: "Tinos", "Times New Roman", serif; font-size: 25px; line-height: 39px;
    color: var(--text-white);
  }
  .credentials {
    position: absolute; left: 40px; top: 405px;
    font-family: "Tinos", "Times New Roman", serif; font-weight: 700; font-size: 25px; line-height: 32px;
    color: var(--text-white);
  }
  .experience-band {
    position: absolute; left: 0; bottom: 0; width: 100%; height: 80px;
    background: var(--band-blue);
    clip-path: polygon(0 0, 62% 0, 64% 30%, 100% 30%, 100% 100%, 0 100%);
    padding: 14px 0 0 30px;
    font-family: "Exo 2", sans-serif; font-weight: 900; font-style: italic;
    font-size: 42px; letter-spacing: 4px; color: var(--logo-yellow);
  }
  .work-photos { position: absolute; right: 40px; top: 250px; width: 300px; height: 300px; }
</style>
</head>
<body>
<div class="canvas">

  <section class="card card--back" aria-label="Business card reverse: services">
    <div class="glow-band glow-band--top" role="img" aria-label="Electric arc artwork across the top edge"></div>
    <div class="glow-band glow-band--bottom" role="img" aria-label="Electric arc artwork across the bottom edge"></div>

    <ul class="services">
      <li><svg viewBox="0 0 20 26"><polygon points="12,0 2,15 9,15 6,26 18,9 11,9" fill="var(--logo-yellow)"/></svg>Domestic, commercial and agricultural work.</li>
      <li><svg viewBox="0 0 20 26"><polygon points="12,0 2,15 9,15 6,26 18,9 11,9" fill="var(--logo-yellow)"/></svg>Inspection and Testing.</li>
      <li><svg viewBox="0 0 20 26"><polygon points="12,0 2,15 9,15 6,26 18,9 11,9" fill="var(--logo-yellow)"/></svg>Rewires.</li>
      <li><svg viewBox="0 0 20 26"><polygon points="12,0 2,15 9,15 6,26 18,9 11,9" fill="var(--logo-yellow)"/></svg>Fuseboards.</li>
      <li><svg viewBox="0 0 20 26"><polygon points="12,0 2,15 9,15 6,26 18,9 11,9" fill="var(--logo-yellow)"/></svg>New builds.</li>
      <li><svg viewBox="0 0 20 26"><polygon points="12,0 2,15 9,15 6,26 18,9 11,9" fill="var(--logo-yellow)"/></svg>Fault finding.</li>
      <li><svg viewBox="0 0 20 26"><polygon points="12,0 2,15 9,15 6,26 18,9 11,9" fill="var(--logo-yellow)"/></svg>Free no obligation quotation.</li>
      <li><svg viewBox="0 0 20 26"><polygon points="12,0 2,15 9,15 6,26 18,9 11,9" fill="var(--logo-yellow)"/></svg>All work undertaken.</li>
    </ul>

    <div class="brand"><span class="brand__square"></span><span class="brand__name">KT ELECTRICAL</span></div>
  </section>

  <section class="card card--front" aria-label="Business card front: contact details">
    <div class="glow-band glow-band--top" role="img" aria-label="Electric arc artwork across the top edge"></div>

    <h1 class="holder-name">Kevin Tallis</h1>
    <div class="brand"><span class="brand__square"></span><span class="brand__name">KT ELECTRICAL</span></div>

    <div class="contact-band">
      <p>Mob :07700900461</p>
      <p>Home :01632960418</p>
      <p>Email :merrow.kt@postvale.com</p>
    </div>

    <p class="credentials">Fully insured and registered with VORSEC.<br>Customer references available on request.</p>

    <div class="experience-band">10 YEARS EXPERIENCE</div>

    <svg class="work-photos" viewBox="0 0 300 300" role="img" aria-label="Three hexagon photos of an electrician wiring a box, fitting a board and testing a circuit">
      <defs>
        <linearGradient id="hexWarm" x1="0" y1="0" x2="1" y2="1"><stop offset="0" stop-color="#b47a52"/><stop offset="1" stop-color="#6e4a3a"/></linearGradient>
        <linearGradient id="hexBoard" x1="0" y1="0" x2="1" y2="1"><stop offset="0" stop-color="#d9d2c4"/><stop offset="1" stop-color="#8a7b6a"/></linearGradient>
        <linearGradient id="hexPanel" x1="0" y1="0" x2="1" y2="1"><stop offset="0" stop-color="#9aa3b0"/><stop offset="1" stop-color="#d6a23a"/></linearGradient>
      </defs>
      <polygon points="40,10 100,10 130,70 100,130 40,130 10,70" fill="url(#hexWarm)" stroke="var(--hex-border)" stroke-width="5"/>
      <polygon points="180,10 240,10 270,70 240,130 180,130 150,70" fill="url(#hexBoard)" stroke="var(--hex-border)" stroke-width="5"/>
      <polygon points="110,150 170,150 200,210 170,270 110,270 80,210" fill="url(#hexPanel)" stroke="var(--hex-border)" stroke-width="5"/>
    </svg>
  </section>

</div>
</body>
</html>
```